Three Self-help Book Covers for MWA

We need three book covers designed.

We have a good idea what the three designs will be and our directions are attached along with sample artwork.

1-Nine Quiet Harbors
2-The PathWay Almanac
3-The Threshold

My schools website is: www.MeadowbrookWellnessAcademy.example

Target Market(s)

Self-help

Industry/Entity Type

Life Coaching

Font styles to use
Other font styles liked:
• See Attachment for details

Requirements
Must have
• See Attached Suggestions
Nice to have
Should not have

```html
<!DOCTYPE html>
<html lang="en">
<head>
<meta charset="utf-8">
<title>The Threshold – Book Cover Wrap</title>
<link rel="stylesheet" href="https://fonts.googleapis.com/css2?family=Quicksand:wght@300;700&family=Tinos:wght@400;700&display=swap">
<style>
  :root {
    --leaf-light: #c9df8a;
    --leaf-mid: #9fc35a;
    --leaf-deep: #4f7f2a;
    --moss: #3c6a22;
    --blossom: #e6c39a;
    --spine-shade: rgba(34, 66, 18, 0.55);
    --ink-dark: #1c2a10;
    --text-light: #ffffff;
    --badge-bg: #ffffff;
    --badge-tone: #a69d80;
  }
  * { margin: 0; padding: 0; box-sizing: border-box; }
  html, body { width: 1200px; height: 800px; overflow: hidden; background: #ffffff; }
  .cover-wrap { position: relative; width: 1200px; height: 800px; overflow: hidden; }
  .cover-artwork {
    position: absolute; inset: 0;
    background:
      radial-gradient(ellipse at 85% 25%, var(--blossom) 0%, rgba(230,195,154,0) 30%),
      radial-gradient(ellipse at 75% 38%, var(--leaf-light) 0%, rgba(201,223,138,0) 45%),
      radial-gradient(ellipse at 20% 35%, var(--leaf-light) 0%, rgba(201,223,138,0) 50%),
      linear-gradient(180deg, var(--leaf-mid) 0%, var(--leaf-deep) 70%, var(--moss) 100%);
  }
  .spine-band {
    position: absolute; left: 525px; top: 0; width: 95px; height: 800px;
    background: var(--spine-shade);
  }
  .back-blurb {
    position: absolute; left: 6px; top: 151px; width: 510px;
    font-family: "Tinos", serif; font-weight: 700; font-size: 19px;
    line-height: 30px; letter-spacing: 4.4px; text-align: center;
    color: var(--ink-dark); white-space: nowrap;
  }
  .publisher-badge {
    position: absolute; left: 381px; top: 658px; width: 144px; height: 142px;
    background: var(--badge-bg);
    display: flex; flex-direction: column; align-items: center; justify-content: center; gap: 10px;
  }
  .publisher-dot { width: 56px; height: 56px; border-radius: 50%; background: var(--badge-tone); }
  .publisher-name {
    font-family: "Tinos", serif; font-weight: 400; font-size: 15px;
    letter-spacing: 1px; color: var(--badge-tone);
  }
  .spine-title, .spine-author {
    position: absolute; writing-mode: vertical-rl; color: var(--text-light); white-space: nowrap;
  }
  .spine-title {
    left: 558px; top: 50px;
    font-family: "Quicksand", sans-serif; font-weight: 300; font-size: 27px; letter-spacing: 10px;
  }
  .spine-author {
    left: 562px; top: 414px;
    font-family: "Tinos", serif; font-weight: 700; font-size: 19px; letter-spacing: 5.4px;
  }
  .front-title {
    position: absolute; left: 667px; top: 18px;
    font-family: "Quicksand", sans-serif; font-weight: 300; font-size: 52px;
    letter-spacing: 9px; color: var(--text-light); white-space: nowrap;
  }
  .front-subtitle {
    position: absolute; left: 630px; top: 396px; width: 560px;
    font-family: "Quicksand", sans-serif; font-weight: 700; font-size: 27px;
    line-height: 52px; letter-spacing: 6.4px; color: var(--text-light);
    text-align: center; white-space: nowrap;
  }
  .front-author {
    position: absolute; left: 648px; top: 730px;
    font-family: "Tinos", serif; font-weight: 400; font-size: 30px;
    letter-spacing: 7.6px; color: var(--text-light); white-space: nowrap;
  }
</style>
</head>
<body>
<main class="cover-wrap">
  <div class="cover-artwork" role="img" aria-label="Soft green photograph of a striped caterpillar on a plant stem, with faint butterflies and pale blossoms blended into the background"></div>
  <div class="spine-band"></div>

  <p class="back-blurb">Lorem ipsum dolor sit amet,<br>consectetur adipiscing elit.<br>Phasellus sit amet magna porta,<br>sollicitudin nibh id, viverra justo.<br>Aliquam bibendum euismod<br>mauris, ac iaculis quam consequat<br>non. Maecenas euismod eget urna<br>sed blandit</p>

  <div class="publisher-badge">
    <span class="publisher-dot"></span>
    <span class="publisher-name">Solace House</span>
  </div>

  <p class="spine-title">The Threshold</p>
  <p class="spine-author">Master Coach Ren Valdemar</p>

  <h1 class="front-title">The Threshold</h1>
  <h2 class="front-subtitle">Toward Your Quiet Courage<br>and Steady Inner Light</h2>
  <p class="front-author">Master Coach Ren Valdemar</p>
</main>
</body>
</html>
```